Business is called "Pelton Ledger". Accounting and tax services.

I need a flyer for my new business "Pelton Ledger". I am an individual accountant working for himself on the Sunshine Coast in Queensland Australia. I would like to see designs that communicate reliability and trust. I believe my point of difference is that I am always available to my clients and I will cap my number of clients to ensure I can service them properly. Accountants in general seem to have a bad reputation for not responding to clients in a timely fashion, whether by email or phone. This is where I intend to differentiate myself. I have included my business card for ideas on colour and for contact information. I have also included some logo's that should go on the flyer. With the QLA logo, the words "Pelton Ledger is a QLA Business" needs to be written either above, below or to the right hand side (as per the business card).

Target Market(s)

Small business owners and individuals requiring taxation and financials

Industry/Entity Type

Public Accounting

Font styles to use
Serif

Requirements
Must have
• Supplied logo's, accounting style pictures etc
Services: Small Business Taxation
Company & Trust Tax Returns
Rental Property Returns
Capital Gains Tax
Individual Tax Returns
BAS and IAS lodgements
Nice to have
• Needs to convey a sense of being reliable and responds to clients quickly.
Should not have
• My name

```html
<!DOCTYPE html>
<html lang="en">
<head>
<meta charset="utf-8">
<title>Pelton Ledger – Flyer</title>
<link rel="stylesheet" href="https://fonts.googleapis.com/css2?family=Lato:ital,wght@1,900&family=Oswald:wght@600&family=Roboto:wght@300;400;700&display=swap">
<style>
  :root {
    --backdrop: #565454;
    --paper: #ffffff;
    --teal: #23b492;
    --teal-soft: #5fcdb2;
    --blue: #0b5ca8;
    --ink: #333333;
    --ink-soft: #555555;
    --badge-ring: #8a8a8a;
    --badge-core: #c3d33a;
    --partner-blue: #1ab4e8;
    --partner-gold: #f5d20a;
  }
  * { margin: 0; padding: 0; box-sizing: border-box; }
  html, body {
    width: 1200px; height: 900px; overflow: hidden;
    background: var(--backdrop);
    font-family: "Roboto", Arial, sans-serif;
  }
  .flyer {
    position: absolute; left: 345px; top: 82px;
    width: 518px; height: 738px;
    background: var(--paper);
    overflow: hidden;
  }
  .flyer-shapes { position: absolute; inset: 0; }
  .brand {
    position: absolute; left: 360px; top: 30px; width: 160px;
    text-align: center; color: #fff;
  }
  .brand-mark {
    display: block; margin: 0 auto 10px;
    width: 38px; height: 38px; border-radius: 50%;
    border: 2px solid #fff;
  }
  .brand-name {
    font-size: 11px; font-weight: 700; letter-spacing: 2.4px; white-space: nowrap;
  }
  .headline {
    position: absolute; left: 195px; top: 220px;
    font-family: "Lato", Arial, sans-serif; font-style: italic; font-weight: 900;
    font-size: 31px; line-height: 37px; color: #fff; letter-spacing: -0.3px;
  }
  .services { position: absolute; left: 207px; top: 394px; }
  .services-title {
    font-family: "Oswald", Arial, sans-serif; font-weight: 600;
    font-size: 17px; color: var(--blue); letter-spacing: 0.2px; margin-bottom: 6px;
  }
  .services-list { list-style: none; }
  .services-list li {
    position: relative; padding-left: 23px;
    font-size: 15px; font-weight: 300; color: var(--ink);
    height: 32.6px; line-height: 32.6px;
  }
  .services-list li::before {
    content: ""; position: absolute; left: 4px; top: 11px;
    width: 10px; height: 10px; border-radius: 50%; background: var(--teal);
  }
  .agent {
    position: absolute; left: 17px; top: 500px; width: 100px;
    text-align: center; font-size: 9.5px; line-height: 12px; color: var(--ink);
  }
  .contact { position: absolute; left: 22px; top: 570px; list-style: none; }
  .contact li {
    display: flex; align-items: center; gap: 8px;
    font-size: 10.5px; color: var(--ink-soft); height: 20px;
  }
  .contact svg { width: 11px; height: 11px; fill: #444; }
  .website {
    position: absolute; left: 110px; top: 697px;
    display: flex; align-items: center; gap: 6px;
    font-size: 12.5px; font-weight: 700; color: #2a2a2a;
  }
  .website svg { width: 16px; height: 16px; }
  .partner {
    position: absolute; top: 697px;
    display: flex; align-items: center; gap: 4px;
    font-size: 11px; font-weight: 700; color: var(--ink);
  }
  .partner-ledgra { left: 318px; }
  .partner-ledgra i { width: 10px; height: 10px; border-radius: 50%; background: var(--partner-blue); }
  .partner-qla { left: 378px; }
  .partner-qla i { width: 10px; height: 10px; background: var(--partner-gold); }
  .membership {
    position: absolute; left: 433px; top: 697px;
    font-size: 7.6px; font-style: italic; line-height: 10px; color: #222;
  }
</style>
</head>
<body>
<main class="flyer">
  <svg class="flyer-shapes" viewBox="0 0 518 738">
    <defs>
      <linearGradient id="photoTone" x1="0" y1="0" x2="1" y2="1">
        <stop offset="0" stop-color="#1b7f6d"/>
        <stop offset="0.55" stop-color="#115f53"/>
        <stop offset="1" stop-color="#0c4a41"/>
      </linearGradient>
      <linearGradient id="chartTone" x1="0" y1="0" x2="0" y2="1">
        <stop offset="0" stop-color="var(--teal-soft)"/>
        <stop offset="1" stop-color="var(--teal)"/>
      </linearGradient>
    </defs>
    <polygon role="img" aria-label="Photo of accountants working at a desk with laptops and paperwork, in a teal tint"
             points="0,0 518,0 518,347 98,347 107,286 0,326" fill="url(#photoTone)"/>
    <polygon points="0,0 70,0 0,70" fill="var(--blue)"/>
    <polygon points="0,326 107,286 98,347 0,407" fill="var(--teal)"/>
    <rect x="96" y="347" width="422" height="2" fill="var(--teal)"/>
    <polygon points="179,218 518,218 518,306 207,306" fill="var(--teal)"/>

    <circle cx="67" cy="459" r="33" fill="#fff" stroke="var(--badge-ring)" stroke-width="2"/>
    <circle cx="67" cy="459" r="19" fill="var(--badge-core)"/>

    <rect role="img" aria-label="Decorative growth chart graphic in teal"
          x="0" y="642" width="106" height="96" fill="url(#chartTone)" opacity="0.85"/>
  </svg>

  <div class="brand">
    <span class="brand-mark"></span>
    <span class="brand-name">PELTON LEDGER</span>
  </div>

  <h1 class="headline">MAKING RETURNS<br>EASY FOR YOU</h1>

  <section class="services">
    <h2 class="services-title">SERVICES</h2>
    <ul class="services-list">
      <li>Small Business Taxation</li>
      <li>Company &amp; Trust Tax Returns</li>
      <li>BAS and IAS lodgements</li>
      <li>Capital Gains Tax</li>
      <li>Individual Tax Returns</li>
      <li>Rental Property Returns</li>
    </ul>
  </section>

  <p class="agent">Tax agent<br>31079258</p>

  <ul class="contact">
    <li><svg viewBox="0 0 24 24"><path d="M6.6 10.8a15 15 0 0 0 6.6 6.6l2.2-2.2c.3-.3.7-.4 1-.2 1.1.4 2.3.6 3.6.6.6 0 1 .4 1 1V20c0 .6-.4 1-1 1A17 17 0 0 1 3 4c0-.6.4-1 1-1h3.5c.6 0 1 .4 1 1 0 1.3.2 2.5.6 3.6.1.3 0 .7-.2 1z"/></svg>0412 586 309</li>
    <li><svg viewBox="0 0 24 24"><path d="M2 5h20v14H2zm2 2v.5l8 5 8-5V7l-8 5z"/></svg>hello@peltonledger.com.au</li>
  </ul>

  <p class="website">
    <svg viewBox="0 0 24 24"><circle cx="12" cy="12" r="10" fill="none" stroke="#333" stroke-width="2"/><path d="M2 12h20M12 2c3 3 3 17 0 20M12 2c-3 3-3 17 0 20" fill="none" stroke="#333" stroke-width="1.5"/></svg>
    www.peltonledger.com.au
  </p>

  <p class="partner partner-ledgra"><i></i>Ledgra</p>
  <p class="partner partner-qla"><i></i>QLA</p>
  <p class="membership">Pelton Ledger<br>is a QLA Business</p>
</main>
</body>
</html>
```